Water ATM Card

Need a design for water ATM cards. Size of card is 3.375 x 2.125 inch
On the Front include the Cedar brook Logo.
Bottom right corner should have Price $100
On the Back
This card is to be used to access water refills at any Cedar Brook Water Vending Machines.
Please contact (869) 614 2938 or (869) 731 4072 or email clearflowhq@examplemail.com for any assistance or recharging of card.

```html
<!DOCTYPE html>
<html lang="en">
<head>
<meta charset="utf-8">
<title>Cedar Brook Water ATM Card</title>
<link rel="stylesheet" href="https://fonts.googleapis.com/css2?family=Bebas+Neue&family=Montserrat:wght@600;700&display=swap">
<style>
  :root {
    --page-bg: #2b2b2d;
    --card-blue: #1f7fd6;
    --card-blue-deep: #1667bd;
    --water-light: #e8f3fb;
    --water-mid: #a9d3f2;
    --water-clear: rgba(169, 211, 242, 0);
    --white: #ffffff;
    --ink: #111417;
    --banner-text: #1868b8;
    --banner-accent: #4caf3c;
  }
  * { box-sizing: border-box; margin: 0; padding: 0; }
  html, body {
    width: 1200px; height: 904px; overflow: hidden;
    background: var(--page-bg);
  }
  .canvas {
    width: 1200px; height: 904px;
    display: flex; flex-direction: column; align-items: center; justify-content: center;
    gap: 30px;
  }
  .card {
    position: relative;
    width: 640px; height: 403px;
    border-radius: 6px;
    overflow: hidden;
    background: linear-gradient(160deg, var(--card-blue) 0%, var(--card-blue-deep) 100%);
    box-shadow: 0 14px 30px rgba(0,0,0,0.45);
  }
  .water-splash {
    position: absolute; left: 0; right: 0; bottom: 0;
  }
  .card--back .water-splash {
    height: 46%;
    background: linear-gradient(180deg, var(--water-clear) 0%, rgba(169,211,242,0.5) 28%, var(--water-mid) 62%, var(--water-light) 100%);
  }
  .card--front .water-splash {
    height: 42%;
    background: linear-gradient(180deg, var(--water-clear) 0%, rgba(169,211,242,0.55) 30%, var(--water-mid) 60%, var(--water-light) 100%);
  }
  .back-heading {
    position: absolute; top: 26px; left: 30px; right: 30px;
    font-family: "Bebas Neue", "Oswald", sans-serif;
    color: var(--white);
    font-size: 33px; line-height: 1.05; letter-spacing: 0.5px;
    text-align: center;
  }
  .brand-name {
    position: absolute; left: 0; right: 0;
    display: flex; align-items: center; justify-content: center; gap: 14px;
    font-family: "Montserrat", sans-serif; font-weight: 700;
    color: var(--white); letter-spacing: 2px;
    line-height: 1;
  }
  .brand-mark {
    width: 20px; height: 20px; border-radius: 50%;
    background: var(--white);
  }
  .card--back .brand-name { top: 130px; font-size: 38px; }
  .card--front .brand-name { top: 160px; font-size: 48px; }
  .card--front .brand-mark { width: 26px; height: 26px; }
  .contact {
    position: absolute; left: 30px; right: 30px; bottom: 50px;
    font-family: "Montserrat", sans-serif; font-weight: 700;
    color: var(--ink);
    font-size: 20px; line-height: 1.35; text-align: center;
  }
  .atm-banner {
    position: absolute; top: 40px; left: 34px; right: 34px;
    height: 62px;
    border-radius: 31px;
    background: var(--white);
    border-bottom: 4px solid var(--banner-accent);
    display: flex; align-items: center; justify-content: center;
    font-family: "Bebas Neue", "Oswald", sans-serif;
    color: var(--banner-text);
    font-size: 42px; letter-spacing: 0.5px;
    padding-top: 4px;
  }
  .price {
    position: absolute; right: 34px; bottom: 110px;
    font-family: "Montserrat", sans-serif; font-weight: 700;
    color: var(--ink); font-size: 30px;
  }
</style>
</head>
<body>
<main class="canvas">
  <section class="card card--back" aria-label="Card back">
    <div class="water-splash" role="img" aria-label="Photograph of splashing clear water with bubbles"></div>
    <p class="back-heading">This card is to be used to access water refills<br>at any Cedar Brook water vending machines.</p>
    <div class="brand-name"><span class="brand-mark"></span>CEDAR BROOK</div>
    <p class="contact">Contact (869) 614 2938 or (869) 731 4072<br>or email clearflowhq@examplemail.com<br>for any assistance or recharging of card.</p>
  </section>

  <section class="card card--front" aria-label="Card front">
    <div class="water-splash" role="img" aria-label="Photograph of a wave of clear water with bubbles"></div>
    <div class="atm-banner">Cedar Brook Water ATM Card</div>
    <div class="brand-name"><span class="brand-mark"></span>CEDAR BROOK</div>
    <p class="price">Price $100</p>
  </section>
</main>
</body>
</html>
```